RBH Be The Man

I need a 2 sided flyer 8.5x11. I want the design to be similar and the words on the front to be the same as attached. Instead of the stadium on right side, use the pics attached.
The following Words/quotes on the back of flyer other pictures:
—Take the road less travelled and watch it make ALL the difference...

—My sons wanted to stay at RBH because they had teachers and coaches that truly cared about them in the classroom and on the field and court. Does your son want to be a big fish in a little pond or a little fish in a big pond?Lorna Veal, Parent of Dominic ‘16 and Gus ‘18

—The kids and teachers at RBH lift each other up. Everyone is raised up by higher expectations and standards of performance, work ethic and behavior. Mark Tobin, Parent Of Harrison ‘18

—Ultimately RBH prepared me for college and the challenges of being a student-athlete at the University of Brennford. I was better prepared to balance school and baseball compared to my fellow teammates from different high schools around the country.

Gus Harlow ‘13, NPL First Round draft pick of NJ Herons

```html
<!DOCTYPE html>
<html lang="en">
<head>
<meta charset="utf-8">
<title>RBH Be The Man Flyer</title>
<link href="https://fonts.googleapis.com/css2?family=Russo+One&family=Open+Sans:wght@600;700&display=swap" rel="stylesheet">
<style>
  :root {
    --stage: #d9dadc;
    --sky-top: #2f6fd0;
    --sky-mid: #8fb4e4;
    --hill: #6f8f4a;
    --trail: #a88e60;
    --blue-deep: #0d4fb0;
    --blue-bright: #1e8ce6;
    --gold: #fbb612;
    --white: #ffffff;
    --ink: #1b1b1b;
  }
  * { box-sizing: border-box; margin: 0; padding: 0; }
  html, body { width: 1200px; height: 675px; overflow: hidden; }
  body { background: var(--stage); position: relative; font-family: "Open Sans", Arial, sans-serif; }

  .flyer {
    position: absolute;
    top: 107px;
    width: 560px;
    height: 460px;
    overflow: hidden;
    box-shadow: 0 6px 18px rgba(0,0,0,.35);
  }
  .flyer--front { left: 27px; }
  .flyer--back { left: 613px; }

  /* Front */
  .front-scene {
    position: absolute; inset: 0;
    background:
      radial-gradient(ellipse 120px 190px at 78% 80%, rgba(40,60,210,.85), rgba(40,60,210,0) 100%),
      radial-gradient(ellipse 140px 110px at 20% 85%, rgba(20,20,20,.8), rgba(20,20,20,0) 100%),
      linear-gradient(180deg, var(--sky-top) 0%, var(--sky-mid) 42%, #7d8f7a 55%, var(--hill) 68%, var(--trail) 100%);
  }
  .brand-mark {
    position: absolute; top: 14px; left: 0; right: 0;
    display: flex; justify-content: center; align-items: center; gap: 6px;
    font-family: "Russo One", Arial, sans-serif; font-size: 16px; color: var(--white);
  }
  .brand-mark__dot { width: 12px; height: 12px; border-radius: 50%; background: var(--white); }
  .front-headline {
    position: absolute; top: 46px; left: 0; right: 0; text-align: center;
    font-family: "Russo One", Arial, sans-serif; color: var(--white);
    text-transform: uppercase; line-height: 1;
    text-shadow: 0 3px 6px rgba(0,0,0,.35);
  }
  .front-headline__lead { display: block; font-size: 40px; letter-spacing: 1px; }
  .front-headline__main { display: block; font-size: 150px; letter-spacing: 2px; margin-top: 4px; }

  /* Back */
  .back-scene {
    position: absolute; inset: 0;
    background:
      radial-gradient(circle 150px at 88% 30%, rgba(70,150,240,.9), rgba(70,150,240,0) 100%),
      radial-gradient(circle 120px at 90% 85%, rgba(10,30,70,.7), rgba(10,30,70,0) 100%),
      linear-gradient(135deg, var(--blue-bright) 0%, var(--blue-deep) 60%, #0a3a88 100%);
  }
  .back-title {
    position: absolute; top: 18px; left: 22px; right: 60px;
    font-family: "Russo One", Arial, sans-serif; color: var(--gold);
    text-transform: uppercase; line-height: 1.05; text-align: center;
    text-shadow: 0 2px 3px rgba(0,0,0,.4);
  }
  .back-title__lead { display: block; font-size: 22px; }
  .back-title__main { display: block; font-size: 29px; }

  .testimonial {
    position: absolute;
    background: var(--gold);
    padding: 10px 16px 10px 16px;
  }
  .testimonial__quote {
    color: var(--white); font-weight: 700; font-size: 12.5px; line-height: 1.3;
    text-shadow: 0 1px 2px rgba(0,0,0,.25);
  }
  .testimonial__author {
    margin-top: 6px;
    font-family: "Russo One", Arial, sans-serif; font-size: 12px;
    color: var(--ink); text-transform: uppercase; letter-spacing: .5px;
  }
  .testimonial--one { left: 0; top: 104px; width: 400px; border-radius: 0 12px 12px 0; }
  .testimonial--two { right: 0; top: 228px; width: 360px; border-radius: 12px 0 0 12px; text-align: right; }
  .testimonial--three { left: 0; top: 322px; width: 430px; border-radius: 0 12px 12px 0; }
</style>
</head>
<body>

<section class="flyer flyer--front">
  <div class="front-scene" role="img" aria-label="Mountain trail landscape with a football player in a blue jersey number 16 facing a school road sign, a group of student silhouettes on the path, and a team running onto the field"></div>
  <div class="brand-mark"><span class="brand-mark__dot"></span>RBH</div>
  <h1 class="front-headline">
    <span class="front-headline__lead">Don’t be a guy, be</span>
    <span class="front-headline__main">The Guy</span>
  </h1>
</section>

<section class="flyer flyer--back">
  <div class="back-scene" role="img" aria-label="Close-up of players in blue RBH helmets huddled together"></div>
  <h2 class="back-title">
    <span class="back-title__lead">Take the road less travelled and</span>
    <span class="back-title__main">Watch it make all the difference...</span>
  </h2>

  <blockquote class="testimonial testimonial--one">
    <p class="testimonial__quote">My sons wanted to stay at RBH because they had teachers and coaches that truly cared about them in the classroom and on the field and court. Does your son want to be a big fish in a little pond or a little fish in a big pond?</p>
    <p class="testimonial__author">— Lorna Veal, Parent of Dominic ’16 and Gus ’18</p>
  </blockquote>

  <blockquote class="testimonial testimonial--two">
    <p class="testimonial__quote">The kids and teachers at RBH lift each other up. Everyone is raised up by higher expectations and standards of performance, work ethic and behavior.</p>
    <p class="testimonial__author">— Mark Tobin, Parent of Harrison ’18</p>
  </blockquote>

  <blockquote class="testimonial testimonial--three">
    <p class="testimonial__quote">Ultimately RBH prepared me for college and the challenges of being a student-athlete at the University of Brennford. I was better prepared to balance school and baseball compared to my fellow teammates from different high schools around the country.</p>
    <p class="testimonial__author">— Gus Harlow ’13, NPL First Round Draft Pick of NJ Herons</p>
  </blockquote>
</section>

</body>
</html>
```